Project Sign for Construction Company

Site contractor needs a 4'x8' sign to place on construction sites for advertising. Our company builds the infrastructure for new housing developments. These sign will be posted on the road side to be viewed by passing cars. I want a clean and bold look and feel that resembles my company logo.

Font styles to use
Other font styles liked:
• Hypatia Sans Pro

Colors

Designer to choose colors to be used in the design.

Requirements
Must have
• 555-382-9146 | Info@MarlowPaving.example
• CUC 8047319
• www.MarlowPaving.example
• Services
• Road Construction
• Site Preparation & Excavation
• Underground Utilities
• Shoreline Restoration
Nice to have
• Now Hiring
• Pipe Layers
• Foremen
• Equipment Operators
Should not have
• Should not have stock picture images used in the design, focus on logo and geometric shapes

```html
<!DOCTYPE html>
<html lang="en">
<head>
<meta charset="utf-8">
<title>Marlow Paving – Site Sign</title>
<link rel="stylesheet" href="https://fonts.googleapis.com/css2?family=Montserrat:ital,wght@0,500;0,600;0,700;0,800;1,800&display=swap">
<style>
  :root {
    --brand-blue: #2f4fa3;
    --brand-blue-deep: #24408f;
    --brand-blue-light: #3a5db3;
    --ink-navy: #1f3a8c;
    --ink-gray: #3b3f4a;
    --panel-white: #ffffff;
    --panel-silver: #e4e6ea;
    --page-bg: #eef0f3;
    --frame: #c9ccd1;
  }
  html, body {
    margin: 0; padding: 0;
    width: 1200px; height: 934px;
    overflow: hidden;
    background: var(--page-bg);
    font-family: "Montserrat", Arial, sans-serif;
  }
  .sign {
    position: absolute;
    left: 40px; top: 187px;
    width: 1120px; height: 560px;
    box-shadow: 0 0 0 6px var(--frame);
    overflow: hidden;
  }
  .sign-art { position: absolute; inset: 0; }
  .megaphone-art {
    position: absolute;
    left: 118px; top: 46px; width: 185px; height: 185px;
    background: radial-gradient(circle at 45% 55%, rgba(255,255,255,0.55), rgba(255,255,255,0.12) 65%, transparent 72%);
  }
  .hiring-headline {
    position: absolute;
    left: 285px; top: 70px;
    transform: rotate(-7deg);
    transform-origin: left bottom;
    color: var(--panel-white);
    font-weight: 800; font-style: italic;
    line-height: 0.9;
  }
  .hiring-headline .now { display: block; font-size: 36px; margin-left: 78px; }
  .hiring-headline .hiring { display: block; font-size: 62px; letter-spacing: 2px; }
  .job-list {
    position: absolute;
    left: 372px; top: 183px; width: 325px; height: 142px;
    background: var(--panel-white);
    border-radius: 32px 4px 4px 32px;
    box-sizing: border-box;
    padding: 12px 0 0 40px;
    margin: 0; list-style: none;
  }
  .job-list li {
    color: var(--ink-navy);
    font-weight: 700; font-size: 27px;
    font-variant: small-caps; letter-spacing: 1px;
    line-height: 31px;
    position: relative;
  }
  .job-list li.arrow::before {
    content: "➜"; position: absolute; left: -30px; font-size: 20px; top: 0;
  }
  .services {
    position: absolute; left: 134px; top: 320px;
    color: var(--panel-white);
  }
  .services h2 {
    margin: 0 0 10px; font-size: 30px; font-weight: 600; letter-spacing: 1px;
  }
  .services ul { margin: 0; padding: 0 0 0 24px; list-style: none; }
  .services li {
    font-size: 20px; font-weight: 600; font-variant: small-caps;
    letter-spacing: 1.5px; line-height: 23px; position: relative;
  }
  .services li::before {
    content: ""; position: absolute; left: -22px; top: 9px;
    width: 7px; height: 7px; border-radius: 50%; background: var(--panel-white);
  }
  .brand-block {
    position: absolute; left: 740px; top: 70px; width: 370px;
    text-align: center;
  }
  .brand-mark {
    width: 70px; height: 70px; margin: 0 auto 26px;
    border: 4px solid var(--ink-navy); box-sizing: border-box;
  }
  .brand-name {
    color: var(--ink-navy); font-weight: 800; font-size: 52px;
    letter-spacing: 3px; line-height: 1; margin: 0;
  }
  .brand-rule {
    position: absolute; left: 738px; top: 323px; width: 370px; height: 2px;
    background: #8b8f98;
  }
  .contact {
    position: absolute; left: 738px; top: 335px; width: 370px;
    text-align: center; font-style: normal;
  }
  .contact .phone {
    display: block; color: var(--ink-navy); font-weight: 800;
    font-size: 38px; letter-spacing: 1px; margin-bottom: 4px;
  }
  .contact .line {
    display: block; color: var(--ink-gray); font-weight: 600;
    font-size: 21px; font-variant: small-caps; letter-spacing: 1px; line-height: 26px;
  }
</style>
</head>
<body>
<main class="sign">
  <svg class="sign-art" width="1120" height="560" viewBox="0 0 1120 560" aria-hidden="true">
    <defs>
      <linearGradient id="blueField" x1="0" y1="0" x2="1" y2="1">
        <stop offset="0" stop-color="var(--brand-blue-light)"/>
        <stop offset="1" stop-color="var(--brand-blue-deep)"/>
      </linearGradient>
      <linearGradient id="silverField" x1="0" y1="0" x2="1" y2="1">
        <stop offset="0" stop-color="var(--panel-silver)"/>
        <stop offset="0.5" stop-color="var(--panel-white)"/>
        <stop offset="1" stop-color="#d9dce1"/>
      </linearGradient>
    </defs>
    <rect width="1120" height="560" fill="url(#silverField)"/>
    <polygon points="0,0 755,0 668,560 0,560" fill="url(#blueField)"/>
    <polygon points="755,0 770,0 683,560 668,560" fill="var(--brand-blue-deep)"/>
    <g stroke="#ffffff" stroke-width="2" fill="none" opacity="0.9">
      <line x1="0" y1="58" x2="195" y2="58"/>
      <line x1="56" y1="40" x2="56" y2="560"/>
      <line x1="0" y1="475" x2="660" y2="475"/>
      <line x1="560" y1="68" x2="745" y2="68"/>
      <line x1="650" y1="30" x2="565" y2="80"/>
      <line x1="35" y1="345" x2="210" y2="255"/>
      <line x1="700" y1="60" x2="640" y2="480"/>
    </g>
  </svg>

  <div class="megaphone-art" role="img" aria-label="Sketch of a megaphone with a burst of sound lines"></div>

  <h1 class="hiring-headline"><span class="now">NOW</span><span class="hiring">HIRING</span></h1>

  <ul class="job-list">
    <li class="arrow">Pipe Layers</li>
    <li class="arrow">Foremen</li>
    <li class="arrow">Equipment</li>
    <li>Operators</li>
  </ul>

  <section class="services">
    <h2>SERVICES</h2>
    <ul>
      <li>Road Construction</li>
      <li>Site Preparation &amp; Excavation</li>
      <li>Underground Utilities</li>
      <li>Shoreline Restoration</li>
    </ul>
  </section>

  <div class="brand-block">
    <div class="brand-mark"></div>
    <p class="brand-name">MARLOW<br>PAVING</p>
  </div>

  <div class="brand-rule"></div>

  <address class="contact">
    <span class="phone">555-382-9146</span>
    <span class="line">Info@MarlowPaving.example</span>
    <span class="line">CUC 8047319</span>
    <span class="line">www.MarlowPaving.example</span>
  </address>
</main>
</body>
</html>
```